Wine Label for a White and a Red Wine from Italy

We have a very good idea of what we want with artwork. We need you to please design a 'template' with the text so we can change out the artwork from year to year. Samples are shown of what we are looking for. We are looking for options with the two basic designs. Brand name of wine is: Valora di Castegno. Both wines are in a light green Bordeaux-style bottle (note: we don't show a light green bottle in the mockup but please remember the bottle is light green). Artwork is provided. We'd like to see either the green or blue butterfly on the white wine, the red butterfly is for the red wine. Please base the design on the attached label from Brailey and/or the attached label from Chateau Mervanges.

Target Market(s)

Millennials, women

Requirements
Must have
• The artwork (butterflies) attached.
Nice to have
• Elegant, readable fonts. Please make the text so it can be changed by the printer. Please make it so the artwork can be changed too.

```html
<!DOCTYPE html>
<html lang="en">
<head>
<meta charset="utf-8">
<title>Valora di Castegno – Barrel Select Labels</title>
<link rel="stylesheet" href="https://fonts.googleapis.com/css2?family=Marcellus&family=Montserrat:wght@500;600&family=Pinyon+Script&display=swap">
<style>
  :root {
    --page: #ffffff;
    --label: #f4f4f5;
    --label-edge: #e6e6e8;
    --ink: #1c1c1c;
    --band: #d9d9db;
    --rosso: #8a4a22;
    --verde: #2f7a3a;
    --gold: #e9a920;
    --gold-light: #f7d57a;
    --butterfly-red: #a5231c;
    --butterfly-teal: #1f8a92;
  }
  * { box-sizing: border-box; margin: 0; padding: 0; }
  html, body {
    width: 1200px;
    height: 1195px;
    overflow: hidden;
    background: var(--page);
  }
  .canvas {
    position: relative;
    width: 1200px;
    height: 1195px;
  }
  .label {
    position: absolute;
    top: 334px;
    width: 400px;
    height: 528px;
    background: linear-gradient(90deg, var(--label-edge) 0%, var(--label) 18%, #fbfbfb 50%, var(--label) 82%, var(--label-edge) 100%);
    display: flex;
    flex-direction: column;
    align-items: center;
    text-align: center;
    color: var(--ink);
  }
  .label--rosso { left: 174px; --accent: var(--rosso); }
  .label--verde { left: 626px; --accent: var(--verde); }

  .brand {
    margin-top: 22px;
    font-family: "Marcellus", serif;
    font-size: 48px;
    letter-spacing: 12px;
    line-height: 1;
    padding-left: 12px;
  }
  .brand-sub {
    margin-top: 6px;
    font-family: "Marcellus", serif;
    font-size: 13px;
    letter-spacing: 6px;
    padding-left: 6px;
  }
  .flourish {
    margin-top: 4px;
    width: 120px;
    height: 10px;
  }
  .range {
    margin-top: 10px;
    font-family: "Montserrat", sans-serif;
    font-weight: 600;
    font-size: 16px;
    letter-spacing: 0.5px;
    color: var(--accent);
  }
  .artwork {
    margin-top: 14px;
    width: 350px;
    height: 206px;
  }
  .artwork--rosso {
    background:
      radial-gradient(ellipse 26% 32% at 50% 50%, var(--butterfly-red) 0%, #7d1a14 60%, transparent 100%),
      radial-gradient(ellipse 70% 80% at 45% 50%, var(--gold) 0%, var(--gold-light) 70%, #ffffff 100%);
  }
  .artwork--verde {
    background:
      radial-gradient(ellipse 26% 32% at 52% 50%, var(--butterfly-teal) 0%, #10383d 65%, transparent 100%),
      radial-gradient(ellipse 80% 85% at 50% 50%, var(--gold) 0%, #f2b93a 65%, var(--gold-light) 100%);
  }
  .wine-name {
    margin-top: 20px;
    font-family: "Montserrat", sans-serif;
    font-weight: 600;
    font-size: 22px;
    letter-spacing: 4px;
    padding-left: 4px;
    color: var(--accent);
    line-height: 1;
  }
  .vintage {
    margin-top: 4px;
    font-family: "Montserrat", sans-serif;
    font-weight: 500;
    font-size: 12px;
    letter-spacing: 2px;
  }
  .credits {
    margin-top: 12px;
    font-family: "Pinyon Script", cursive;
    font-size: 17px;
    line-height: 1.3;
  }
  .origin-band {
    margin-top: auto;
    width: 100%;
    height: 40px;
    background: var(--band);
    display: flex;
    align-items: center;
    justify-content: center;
    font-family: "Montserrat", sans-serif;
    font-weight: 600;
    font-size: 14px;
    letter-spacing: 1px;
  }
</style>
</head>
<body>
<main class="canvas">

  <section class="label label--rosso">
    <h1 class="brand">VALORA</h1>
    <p class="brand-sub">DI CASTEGNO</p>
    <svg class="flourish" viewBox="0 0 120 10" aria-hidden="true">
      <path d="M0 3 H50 Q55 3 60 8 Q65 3 70 3 H120" fill="none" stroke="#9a9a9a" stroke-width="1"/>
    </svg>
    <p class="range">BARREL SELECT</p>
    <div class="artwork artwork--rosso" role="img" aria-label="Painted red butterfly over golden yellow brushstrokes"></div>
    <h2 class="wine-name">ROSSO</h2>
    <p class="vintage">2018</p>
    <p class="credits">Artisanally crafted by cantina lusoni<br>Sustainably farmed</p>
    <p class="origin-band">PIEMONTE &nbsp;/&nbsp; ITALY</p>
  </section>

  <section class="label label--verde">
    <h1 class="brand">VALORA</h1>
    <p class="brand-sub">DI CASTEGNO</p>
    <svg class="flourish" viewBox="0 0 120 10" aria-hidden="true">
      <path d="M0 3 H50 Q55 3 60 8 Q65 3 70 3 H120" fill="none" stroke="#9a9a9a" stroke-width="1"/>
    </svg>
    <p class="range">BARREL SELECT</p>
    <div class="artwork artwork--verde" role="img" aria-label="Painted blue-green butterfly over golden yellow brushstrokes"></div>
    <h2 class="wine-name">VERDE</h2>
    <p class="vintage">2018</p>
    <p class="credits">Artisanally crafted by cantina lusoni<br>Sustainably farmed</p>
    <p class="origin-band">PIEMONTE &nbsp;/&nbsp; ITALY</p>
  </section>

</main>
</body>
</html>
```